Pine Ridge Traders, LLC- Global Beverage Company with 100% Cold Chain Logistics

Hey All, My Name is Dale, I am a young business owner in a competitive export space, but my niche is that I am shipping all of my beer around the world, "100% Cold Chain". This model is more costly, but it protects the integrity of the beer itself and will give folks in foreign countries the best representation of what US Craft Beer has to offer.

I am not a branding guy and don't claim to be one, I am a salesperson first, and will be referring to all of you to create something great that will be memorable.

I am looking for a basic Business Card Design for my Craft Beer Export company. I sell US Craft Beer in several countries around the globe. Austrailia, China, Taiwan, Chile, France, New Zealand... to name a few.

I am looking for a sleek, modern, and fresh design. Quickly!

Thanks for your consideration!

Cheers,

Dale

Target Market(s)

International

Contact Information for Business Card

Dale Corwin
Founder- Roving Hops Guy
Dale@PineRidgeTraders.example
@RovingHopsGuy- Instagram only
www.Pineridgetraders.example
@PineRidgeTradersAU- Instagram Only

Font styles to use
Serif

Colors
0592cd
ffffff

Requirements
Must have
• Name-
• Title-
• Email-
• Social Media Handle-
• Company Website-
Nice to have
• Nice Logo/ Images on Card
Should not have
• Tacky Beer Images

```html
<!DOCTYPE html>
<html lang="en">
<head>
<meta charset="utf-8">
<title>Pine Ridge Traders, LLC – Business Card</title>
<link href="https://fonts.googleapis.com/css2?family=Roboto+Condensed:wght@400;500;700&family=Roboto:wght@700&display=swap" rel="stylesheet">
<style>
  :root {
    --backdrop: #18191a;
    --card: #dcdcdc;
    --ink: #0d0d0d;
    --muted: #444444;
    --brand-blue: #1b8dc8;
  }
  html, body {
    margin: 0;
    padding: 0;
    width: 1200px;
    height: 1200px;
    overflow: hidden;
    background: var(--backdrop);
  }
  .canvas {
    position: relative;
    width: 1200px;
    height: 1200px;
  }
  .card {
    position: absolute;
    left: 151px;
    width: 840px;
    height: 480px;
    background: var(--card);
    overflow: hidden;
  }
  .card--front { top: 88px; }
  .card--back { top: 604px; }

  .rule {
    position: absolute;
    height: 3px;
    background: var(--brand-blue);
  }

  .brand-mark {
    position: absolute;
    display: flex;
    flex-direction: column;
    align-items: center;
    justify-content: center;
    gap: 6px;
  }
  .brand-mark__dot {
    border-radius: 50%;
    background: var(--brand-blue);
  }
  .brand-mark__name {
    font-family: "Roboto Condensed", sans-serif;
    font-weight: 700;
    color: var(--brand-blue);
    text-align: center;
    line-height: 1.05;
  }

  .company {
    position: absolute;
    margin: 0;
    font-family: "Roboto Condensed", sans-serif;
    font-weight: 400;
    color: var(--ink);
    white-space: nowrap;
    line-height: 1;
    letter-spacing: -0.5px;
  }
  .company__suffix { color: var(--brand-blue); }

  .tagline {
    position: absolute;
    margin: 0;
    font-family: "Roboto", sans-serif;
    font-weight: 700;
    color: var(--muted);
    white-space: nowrap;
    line-height: 1;
  }

  /* Front */
  .card--front .company { left: 272px; top: 180px; font-size: 44px; }
  .card--front .tagline { left: 274px; top: 250px; font-size: 18px; }

  /* Back */
  .card--back .company { left: 123px; top: 170px; font-size: 37px; }
  .card--back .tagline { left: 124px; top: 232px; font-size: 16px; font-family: "Roboto Condensed", sans-serif; }

  .person {
    position: absolute;
    right: 78px;
    top: 136px;
    text-align: right;
  }
  .person__name {
    margin: 0;
    font-family: "Roboto Condensed", sans-serif;
    font-weight: 700;
    font-size: 46px;
    line-height: 1;
    color: var(--ink);
    letter-spacing: -0.5px;
  }
  .person__surname { color: var(--brand-blue); }
  .person__title {
    margin: 4px 0 0;
    font-family: "Roboto Condensed", sans-serif;
    font-weight: 500;
    font-size: 20px;
    line-height: 1;
    color: var(--ink);
  }

  .contact {
    position: absolute;
    right: 79px;
    top: 292px;
    margin: 0;
    padding: 0;
    list-style: none;
    text-align: right;
    font-family: "Roboto Condensed", sans-serif;
    font-weight: 400;
    font-size: 22px;
    color: var(--muted);
  }
  .contact li { height: 36px; line-height: 36px; }
</style>
</head>
<body>
<div class="canvas">

  <section class="card card--front">
    <div class="rule" style="left:0; width:152px; top:235px;"></div>
    <div class="rule" style="left:273px; right:0; top:235px;"></div>
    <div class="brand-mark" style="left:161px; top:178px; width:102px; height:102px;">
      <span class="brand-mark__dot" style="width:24px; height:24px;"></span>
      <span class="brand-mark__name" style="font-size:14px;">Pine Ridge<br>Traders</span>
    </div>
    <h1 class="company">Pine Ridge Traders, <span class="company__suffix">LLC</span></h1>
    <p class="tagline">Global Beverage Company with 100% Cold Chain Logistics</p>
  </section>

  <section class="card card--back">
    <div class="rule" style="left:0; width:30px; top:215px;"></div>
    <div class="rule" style="left:124px; width:638px; top:215px;"></div>
    <div class="rule" style="left:784px; right:0; top:215px;"></div>
    <div class="brand-mark" style="left:33px; top:171px; width:82px; height:82px;">
      <span class="brand-mark__dot" style="width:20px; height:20px;"></span>
      <span class="brand-mark__name" style="font-size:12px;">Pine Ridge<br>Traders</span>
    </div>
    <h2 class="company">Pine Ridge Traders, LLC</h2>
    <p class="tagline">Global Beverage Company with 100% Cold Chain Logistics</p>

    <div class="person">
      <p class="person__name">Dale <span class="person__surname">Corwin</span></p>
      <p class="person__title">Founder- Roving Hops Guy</p>
    </div>

    <ul class="contact">
      <li>@RovingHopsGuy</li>
      <li>Dale@PineRidgeTraders.example</li>
      <li>www.Pineridgetraders.example</li>
    </ul>
  </section>

</div>
</body>
</html>
```